IT-Dienstleister für Projektmanagementsoftware sucht Broschüre im DIN-A4-Format
Zielgruppe
Wir sind ein IT-Dienstleister für Projektmanagementsoftware. Wir installieren, migrieren und entwickeln Software für das Projektmanagement auf Basis von Veltrano Technologien. Unsere Zielgruppe sind mittelständische Unternehmen und große Konzerne. Je komplexer das Projektmanagement in einem Unternehmen, desto eher helfen unsere Lösungen.
Aufgabenstellung
Es soll eine DIN A4 Hochglanz Broschüre für eine Messe entstehen. Wir haben bereits ein Grobkonzept mit Bildauswahl und Texten erstellt. An diesem soll sich orientiert werden. Bezüglich desDesigns, der Anordnung der Texte und Bilder etc. besteht völlige Freiheit. Weitere Orientierung bieten unsere Webseiten haldewiegand.de und quilbyte.de. Die Texte und Screenshots sind teilweise nur Platzhalter und müssen später noch angepasst werden können. Wir benötigen daher unbedingt die Rohdaten des Designs.

```html
<!DOCTYPE html>
<html lang="de">
<head>
<meta charset="utf-8">
<title>Broschüre Projektmanagement</title>
<link rel="stylesheet" href="https://fonts.googleapis.com/css2?family=Roboto:wght@300;400;500;700&display=swap">
<style>
:root{
  --stage:#d8d8da;
  --divider:#f4f4f4;
  --green:#9cc43a;
  --green-dark:#7fa92a;
  --ink:#3a3a3a;
  --ink-soft:#666;
  --paper:#ffffff;
  --page-grey:#ececec;
  --rule:#cfcfcf;
  --amber:#f0b429;
  --red:#e0453a;
  --ok:#62b346;
  --link:#3d7fc4;
}
*{box-sizing:border-box;margin:0;padding:0}
html,body{width:1200px;height:3551px;overflow:hidden}
body{background:var(--stage);font-family:"Roboto",Arial,sans-serif;color:var(--ink);position:relative}
.band{position:absolute;left:0;width:1200px;height:880px;background:var(--stage)}
.band-1{top:0}.band-2{top:888px}.band-3{top:1776px}.band-4{top:2664px;height:887px}
.spread{position:absolute;left:125px;top:104px;width:950px;height:672px;display:flex;box-shadow:0 6px 18px rgba(0,0,0,.18)}
.page{position:relative;width:475px;height:672px;overflow:hidden;background:var(--paper)}
.page svg.bg{position:absolute;inset:0}
.page-grey{background:linear-gradient(90deg,#dcdcdc 0,#efefef 12%,#f6f6f6 100%)}
/* product pages */
.product-title{position:absolute;left:48px;top:408px;font-weight:300;font-size:38px;color:#fff;letter-spacing:.2px}
.product-sub{position:absolute;left:50px;top:462px;width:330px;font-weight:300;font-size:11.5px;line-height:1.35;color:#fff}
.product-body{position:absolute;left:50px;top:500px;width:320px;font-size:7.6px;line-height:1.5;color:#fff}
.product-body p+p{margin-top:8px}
.sheet{position:absolute;left:44px;top:47px;width:390px;height:565px;background:var(--paper);box-shadow:0 2px 8px rgba(0,0,0,.12);padding:22px 20px}
.shot{border:1px solid var(--rule);font-size:5px;color:var(--ink-soft);margin-bottom:8px}
.shot-head{background:#eef4e4;padding:3px 5px;font-size:6px;color:#557;border-bottom:1px solid var(--rule)}
.shot table{width:100%;border-collapse:collapse}
.shot td{padding:2.5px 4px;border-bottom:1px solid #eee;white-space:nowrap}
.dot{display:inline-block;width:5px;height:5px;border-radius:50%}
.d-ok{background:var(--ok)}.d-am{background:var(--amber)}.d-rd{background:var(--red)}
.lnk{color:var(--link)}
.bar{height:4px;background:#e8e8e8;position:relative}
.bar i{position:absolute;left:0;top:0;bottom:0;background:var(--green)}
.features{list-style:none;font-size:7.6px;line-height:1.4;color:var(--ink);margin-top:14px}
.features li{padding-left:10px;position:relative;margin-bottom:6px}
.features li::before{content:"»";position:absolute;left:0;color:var(--ink-soft)}
/* partner page */
.claim{position:absolute;left:48px;top:398px;width:370px;font-size:11.5px;line-height:1.3;color:var(--green);font-weight:400}
.claim b{font-weight:700}
.claim-body{position:absolute;left:48px;top:460px;width:370px;font-size:7.6px;line-height:1.5;color:var(--ink)}
.tools{position:absolute;left:48px;top:536px;display:flex;align-items:center;gap:18px;font-size:9.5px;color:var(--ink)}
.tool{display:flex;align-items:center;gap:5px}
.tool i{width:11px;height:11px;background:var(--green)}
.partner-badge{width:118px;height:30px;background:#e2e2e2}
.footer-names{position:absolute;left:48px;top:620px;display:flex;gap:28px;align-items:center}
.firm{font-size:11px;font-weight:400;color:var(--ink-soft);display:flex;align-items:center;gap:6px}
.firm i{width:10px;height:10px;border-radius:50%;background:var(--ink-soft)}
/* BI page */
.bi-title{position:absolute;left:55px;top:100px;font-size:12px;color:var(--ink)}
.bi-text{position:absolute;left:55px;top:130px;width:220px;font-size:7.4px;line-height:1.5;color:var(--ink)}
.pbi-title{position:absolute;left:55px;top:428px;font-size:12px;color:var(--ink)}
.pbi-text{position:absolute;left:55px;top:455px;width:285px;font-size:7.4px;line-height:1.5;color:var(--ink)}
/* back cover */
.finale{position:absolute;right:42px;top:400px;width:260px;font-size:21px;line-height:1.15;color:#4a4a4a;text-align:left}
.finale span{color:var(--green)}
.back-firms{position:absolute;left:60px;right:40px;bottom:40px;display:flex;justify-content:space-between;align-items:center}
</style>
</head>
<body>

<!-- Spread 1 -->
<section class="band band-1">
  <div class="spread">
    <div class="page">
      <svg class="bg" width="475" height="672" viewBox="0 0 475 672">
        <defs><linearGradient id="lynx" x1="0" y1="0" x2="1" y2="1"><stop offset="0" stop-color="#6f7f4a"/><stop offset=".55" stop-color="#b39566"/><stop offset="1" stop-color="#d9cdb2"/></linearGradient></defs>
        <rect width="475" height="400" fill="url(#lynx)" role="img" aria-label="Foto eines Leoparden im grünen Geäst"/>
        <polygon points="0,357 475,394 475,672 0,672" fill="var(--green)"/>
      </svg>
      <h1 class="product-title">Quick Lynx</h1>
      <p class="product-sub">Ihre Projektkommunikation einfach standardisiert</p>
      <div class="product-body">
        <p>Quick Lynx vereinfacht das Statusberichtswesen für die Kommunikation zwischen Projekt und Management und erstellt übersichtliche Berichte auf Knopfdruck.</p>
        <p>Die visuell ansprechenden Berichte werden automatisch generiert und sind einfach konfigurierbar. So kann jederzeit auf die individuellen Bedürfnisse Ihres Unternehmens eingegangen werden. Die Reports sorgen für klare Verhältnisse, unabhängig davon ob Sie Ampelsysteme oder Performancewerte bevorzugen.</p>
      </div>
    </div>
    <div class="page page-grey">
      <div class="sheet">
        <div class="shot">
          <div class="shot-head">Projektstatus – Übersicht</div>
          <table>
            <tr><td>Projekt Alpha</td><td><span class="dot d-ok"></span> <span class="dot d-am"></span> <span class="dot d-ok"></span></td><td>09.03.</td><td class="lnk">Bericht 01.pdf</td></tr>
            <tr><td>Projekt Beta</td><td><span class="dot d-am"></span> <span class="dot d-rd"></span> <span class="dot d-ok"></span></td><td>09.03.</td><td class="lnk">Bericht 02.pdf</td></tr>
            <tr><td>Projekt Gamma</td><td><span class="dot d-ok"></span> <span class="dot d-ok"></span> <span class="dot d-am"></span></td><td>09.03.</td><td class="lnk">Bericht 03.pdf</td></tr>
            <tr><td>Migration Server</td><td><span class="dot d-ok"></span> <span class="dot d-am"></span> <span class="dot d-ok"></span></td><td>09.03.</td><td class="lnk">Bericht 04.pdf</td></tr>
            <tr><td>Betrieb</td><td><span class="dot d-ok"></span> <span class="dot d-ok"></span> <span class="dot d-ok"></span></td><td>09.03.</td><td class="lnk">Bericht 05.pdf</td></tr>
          </table>
        </div>
        <div class="shot">
          <div class="shot-head">Statusbericht Projekt Alpha</div>
          <table>
            <tr><td>Meilenstein</td><td>Start</td><td>Ende</td><td style="width:40%"><div class="bar"><i style="width:80%"></i></div></td></tr>
            <tr><td>Konzept</td><td>02.01.</td><td>31.01.</td><td><div class="bar"><i style="width:100%"></i></div></td></tr>
            <tr><td>Umsetzung</td><td>01.02.</td><td>30.04.</td><td><div class="bar"><i style="width:55%"></i></div></td></tr>
            <tr><td>Test</td><td>02.05.</td><td>31.05.</td><td><div class="bar"><i style="width:20%"></i></div></td></tr>
            <tr><td>Abnahme</td><td>01.06.</td><td>15.06.</td><td><div class="bar"><i style="width:0%"></i></div></td></tr>
          </table>
        </div>
        <ul class="features">
          <li><b>revisionssichere Ablage aller Statusberichte:</b> Projektleiter kann manuell Ergänzungen zu automatisch generierten Werten vornehmen</li>
          <li><b>aktuellen Projektstatus</b> jederzeit in leicht verständlichen Berichten im Unternehmen teilen</li>
          <li>Stichtagsbezogene Daten</li>
          <li>Chronologische Darstellung gespeicherter Statusberichte</li>
          <li>Kombination qualitativer und quantitativer Daten</li>
          <li>Meilensteintrendanalyse</li>
          <li>Unkomplizierte Integration</li>
        </ul>
      </div>
    </div>
  </div>
</section>

<!-- Spread 2 -->
<section class="band band-2">
  <div class="spread">
    <div class="page">
      <svg class="bg" width="475" height="672" viewBox="0 0 475 672">
        <defs><linearGradient id="bison" x1="0" y1="0" x2="0" y2="1"><stop offset="0" stop-color="#a9bfd2"/><stop offset=".4" stop-color="#6e6a5c"/><stop offset="1" stop-color="#b7874b"/></linearGradient></defs>
        <rect width="475" height="400" fill="url(#bison)" role="img" aria-label="Foto eines Elefanten in trockener Savanne"/>
        <polygon points="0,357 475,394 475,672 0,672" fill="var(--green)"/>
      </svg>
      <h1 class="product-title">Calm Bison</h1>
      <p class="product-sub">Einfache Abbildung Ihrer Projektstruktur in individuellen Dashboards</p>
      <div class="product-body" style="top:515px">
        <p>Benutzer können sich ihr individuelles Dashboard zusammenstellen und erhalten mit nur einem Klick alle für sie relevanten Projektinformationen.</p>
        <p>Bilden Sie Ihre Projektstruktur ab und erhalten Sie damit bequem Informationen zu dem ausgewählten Projekt. Welche Vorgänge verspätet sind und welche Meilensteine anstehen, behalten Sie genauso im Blick wie den aktuellen Fortschritt.</p>
      </div>
    </div>
    <div class="page page-grey">
      <div class="sheet">
        <div class="shot">
          <div class="shot-head">Portfolio · Dashboard</div>
          <table>
            <tr><td>▸ Bereich Nord</td><td>Zeitplan</td><td style="width:45%"><div class="bar"><i style="width:60%"></i></div></td></tr>
            <tr><td>&nbsp;&nbsp;▸ Projekt Alpha</td><td>Meilenstein</td><td><div class="bar"><i style="width:40%"></i></div></td></tr>
            <tr><td>&nbsp;&nbsp;▸ Projekt Beta</td><td>Verspätet</td><td><div class="bar"><i style="width:75%;background:var(--red)"></i></div></td></tr>
            <tr><td>▸ Bereich Süd</td><td>Zeitplan</td><td><div class="bar"><i style="width:30%"></i></div></td></tr>
          </table>
        </div>
        <div class="shot">
          <div class="shot-head">Projektliste</div>
          <table>
            <tr><td><span class="dot d-ok"></span></td><td class="lnk">Projekt Alpha</td><td>Planung</td><td>42 %</td></tr>
            <tr><td><span class="dot d-am"></span></td><td class="lnk">Projekt Beta</td><td>Umsetzung</td><td>68 %</td></tr>
            <tr><td><span class="dot d-ok"></span></td><td class="lnk">Projekt Gamma</td><td>Test</td><td>85 %</td></tr>
            <tr><td><span class="dot d-rd"></span></td><td class="lnk">Projekt Delta</td><td>Umsetzung</td><td>23 %</td></tr>
            <tr><td><span class="dot d-ok"></span></td><td class="lnk">Projekt Epsilon</td><td>Abschluss</td><td>97 %</td></tr>
          </table>
        </div>
        <ul class="features">
          <li>Hierarchische Darstellung des Projektportfolios</li>
          <li>Dashboard für Projektinformationen</li>
          <li>Navigation, Quicklinks und Informationen über ausgewählte Projekte</li>
          <li>Schnelle Navigation zu wichtigen Projektinhalten</li>
          <li>Quicklinks für intuitive Navigation</li>
          <li>Milestone – Übersichten</li>
          <li>Aktueller Fortschritt im Blick</li>
        </ul>
      </div>
    </div>
  </div>
</section>

<!-- Spread 3 -->
<section class="band band-3">
  <div class="spread">
    <div class="page">
      <svg class="bg" width="475" height="672" viewBox="0 0 475 672">
        <defs><linearGradient id="orbit" x1="0" y1="0" x2="0" y2="1"><stop offset="0" stop-color="#4a4a4e"/><stop offset=".35" stop-color="#6b8fb8"/><stop offset="1" stop-color="#dfe7ef"/></linearGradient></defs>
        <polygon points="0,0 475,0 475,326 0,366" fill="url(#orbit)" role="img" aria-label="Foto eines Astronauten an der Raumstation über der Erde"/>
      </svg>
      <p class="claim">Unser junges und dynamisches Team ist als <b>Veltrano Gold Partner seit 10 Jahren auf Projekt- und Prozessmanagement</b> mit Veltrano Technologien spezialisiert.</p>
      <p class="claim-body">Unsere Spezialisierung auf Portfolio-, Programm- und Projektmanagement mit Veltrano Planwerk und Teilraum und die Abdeckung aller relevanten Fähigkeiten stellen eine kompetente Begleitung Ihrer Projekte sicher.</p>
      <div class="tools">
        <span class="tool"><i></i>Planwerk</span>
        <span class="tool"><i></i>Kontor Suite</span>
        <span class="tool"><i></i>Teilraum</span>
        <span class="partner-badge"></span>
      </div>
      <div class="footer-names">
        <span class="firm"><i></i>Halde &amp; Wiegand</span>
        <span class="firm"><i></i>quilbyte</span>
      </div>
    </div>
    <div class="page">
      <svg class="bg" width="475" height="672" viewBox="0 0 475 672">
        <defs><linearGradient id="greytop" x1="0" y1="0" x2="1" y2="0"><stop offset="0" stop-color="#dcdcdc"/><stop offset=".15" stop-color="#ececec"/><stop offset="1" stop-color="#f3f3f3"/></linearGradient></defs>
        <polygon points="0,0 475,0 475,271 0,312" fill="url(#greytop)"/>
        <rect x="297" y="68" width="178" height="170" fill="#2f3033"/>
        <rect x="306" y="78" width="169" height="152" fill="#e9ecef" role="img" aria-label="Bildschirmfoto eines Business-Intelligence-Dashboards"/>
        <rect x="194" y="326" width="254" height="122" fill="#e6e9ee" role="img" aria-label="Dashboards auf Laptop, Tablet und Smartphone"/>
      </svg>
      <h2 class="bi-title">Business Intelligence und Dashboards</h2>
      <p class="bi-text">Auswertbarkeit ist das A und O einer erfolgreichen Unternehmens- und Projektsteuerung. Reports, Dashboards und Technologien zur Business Intelligence helfen Ihnen, die drängendsten Themen noch besser zu identifizieren. Ob individuell entwickelt oder Ready-to-Use mit Lumetra BI, Halde &amp; Wiegand ist Ihr Partner, um stets den Überblick zu behalten.</p>
      <h2 class="pbi-title">Lumetra BI</h2>
      <p class="pbi-text">Lumetra BI ist eine Suite aus Business Analytics-Tools, die Einblicke in alle Bereiche Ihrer Organisation liefern. Stellen Sie Verbindungen mit Hunderten von Datenquellen her, vereinfachen Sie die Datenaufbereitung, und optimieren Sie Ad-hoc-Analysen. Generieren und veröffentlichen Sie ansprechende Berichte zur unternehmensweiten Nutzung über das Web oder auf mobilen Geräten.</p>
    </div>
  </div>
</section>

<!-- Spread 4 -->
<section class="band band-4">
  <div class="spread">
    <div class="page">
      <svg class="bg" width="475" height="672" viewBox="0 0 475 672">
        <defs><linearGradient id="launch" x1="0" y1="0" x2="1" y2="1"><stop offset="0" stop-color="#3d6ea8"/><stop offset=".5" stop-color="#8fa7c0"/><stop offset="1" stop-color="#d8d6d0"/></linearGradient></defs>
        <rect width="475" height="672" fill="url(#launch)" role="img" aria-label="Foto eines startenden Raumfährenshuttles an der Startrampe"/>
      </svg>
    </div>
    <div class="page">
      <svg class="bg" width="475" height="672" viewBox="0 0 475 672">
        <defs><linearGradient id="dusk" x1="0" y1="0" x2="1" y2="1"><stop offset="0" stop-color="#1f2530"/><stop offset=".6" stop-color="#5a6170"/><stop offset="1" stop-color="#b9bcc2"/></linearGradient></defs>
        <polygon points="0,0 270,0 0,430" fill="url(#dusk)"/>
      </svg>
      <p class="finale">Kommen Sie mit auf unsere digitale Arche Noah in die Zukunft des <span>Projektmanagements!</span></p>
      <div class="back-firms">
        <span class="firm"><i></i>quilbyte</span>
        <span class="firm"><i></i>Halde &amp; Wiegand</span>
      </div>
    </div>
  </div>
</section>

</body>
</html>
```